Bright Cabin Works Needs a Flyer

We need a new flyer for our Garden Nook Tavern. (Photos attached)

We would like to place the bar close to a nice swimming pool that would be in someone's back yard in Florida.

1. Add solar panels. Solar is installed on rails so they sit 2"-3" off the roof.
3. Add a still frame of the Coral Herons football game on the TV.
4. The over all color scheme should be colors that compliment pools and
back patios like blues. Not green or orange. Don't try to match our
logo.

4. Make the bar and pool the central main photo.

Here is some copy for the flyer:

"Your pool is lonely! Introducing our stunning solar powered Garden Nook Tavern!"

"Expand the value of your outdoor living with the ultimate Entertianment venue"

Bullets:

- Dimensions: 5' deep x 10' wide x 9-6'. Enough seating for 6-8 people.
- Comes FULLY assembled. You can't reach this level of quality in a kit.
- 1 coat of primer, two coats of Havelock Prime Glossmark paint for
extreme weather.
- 150 MPH rated Brantley Hale shingles
- TV mount included in the base configuration.
- Options include, pendant lights, hard surface floor, flip up shelf on short
side, bar stools, cabinets, portable sinks, keg tap installs. wine shelves ,
copper wine glasses, liquor shelves and more!

"Solar versions have enough solar and batteries to power your TV, lights, mini fridge, cell phones and more. The advanced Lithium Phosphate Batteries are very safe and can power everything for up to 48 hours without sun."

"Visit our website and mention "Coastal Glow" in the comments section and receive a free Kodo cooler when you order your new Garden Nook Tavern!"

"Visit www.BrightCabinWorks.example/GardenNookTavern to learn more!"

```html
<!DOCTYPE html>
<html lang="en">
<head>
<meta charset="utf-8">
<title>Garden Nook Tavern Flyer</title>
<link rel="stylesheet" href="https://fonts.googleapis.com/css2?family=Lobster&family=Roboto+Condensed:wght@700&family=Source+Sans+3:wght@400;600&display=swap">
<style>
  :root {
    --teal: #1ba3ab;
    --teal-deep: #0d7a86;
    --teal-dark: #0a5f6c;
    --teal-light: #8fd3d6;
    --ink: #2e2e30;
    --cream: #fbf7ec;
    --sky: #cfe6ee;
    --pool: #8fc9da;
    --deck: #a9a2b8;
    --white: #ffffff;
  }
  * { box-sizing: border-box; margin: 0; padding: 0; }
  html, body { width: 846px; height: 1200px; overflow: hidden; background: var(--white); }
  .flyer {
    position: relative; width: 846px; height: 1200px; overflow: hidden;
    background: var(--white);
    font-family: "Source Sans 3", Arial, sans-serif; color: var(--ink);
  }
  .hero-scene {
    position: absolute; left: 0; top: 0; width: 846px; height: 460px;
    background: linear-gradient(180deg, var(--cream) 0%, #f3efe6 30%, var(--sky) 42%, var(--pool) 56%, #b9c3d3 72%, var(--deck) 100%);
  }
  .bar-photo {
    position: absolute; left: 391px; top: 26px; width: 430px; height: 420px;
    border-radius: 6px;
    background: linear-gradient(160deg, #4a4d55 0%, #3a3c42 30%, #8a6a4a 55%, #2f3136 80%, #6b6f7a 100%);
    opacity: .92;
  }
  .headline { position: absolute; left: 36px; top: 22px; }
  .headline-script {
    font-family: "Lobster", cursive; font-size: 37px; color: var(--teal); line-height: 44px;
  }
  .headline-intro {
    font-family: "Roboto Condensed", Arial, sans-serif; font-weight: 700;
    font-size: 24px; line-height: 32px; text-transform: uppercase; margin-top: 6px;
  }
  .headline-intro .dark { color: var(--ink); }
  .headline-intro .accent { color: var(--teal); }
  .top-wave { position: absolute; left: 0; top: 380px; }
  .brand-badge {
    position: absolute; left: 65px; top: 275px; width: 150px; height: 150px;
    border-radius: 50%; background: var(--white); border: 6px solid var(--teal);
    display: flex; align-items: center; justify-content: center; text-align: center;
    font-family: "Roboto Condensed", Arial, sans-serif; font-weight: 700;
    font-size: 20px; line-height: 23px; color: var(--teal-deep); padding: 0 18px;
  }
  .section-heading {
    position: absolute; left: 36px; top: 477px;
    font-family: "Roboto Condensed", Arial, sans-serif; font-weight: 700;
    font-size: 23px; line-height: 32px;
  }
  .section-heading .accent { color: var(--teal); }
  .section-heading .dark { color: var(--ink); }
  .intro-copy {
    position: absolute; left: 36px; top: 585px; width: 370px;
    font-size: 17px; line-height: 25.5px; text-align: justify;
  }
  .detail-photo { position: absolute; border-radius: 8px; }
  .detail-cooler { left: 440px; top: 523px; width: 136px; height: 80px;
    background: linear-gradient(135deg, #3d4148, #b8455a 55%, #7b5a3e); }
  .detail-opener { left: 440px; top: 616px; width: 136px; height: 82px;
    background: linear-gradient(135deg, #cfd6dc, #8a6a4a 60%, #4b3a2c); }
  .detail-wine { left: 585px; top: 523px; width: 222px; height: 175px;
    background: linear-gradient(180deg, #8b5e3a, #3f3a3a 45%, #9a6a45 75%, #6e4a30); }
  .bottom-wave { position: absolute; left: 0; top: 930px; }
  .feature-list {
    position: absolute; left: 438px; top: 722px; width: 372px; list-style: none;
    font-size: 14.5px; line-height: 21px;
  }
  .feature-list li { position: relative; padding-left: 22px; margin-bottom: 7px; text-align: justify; }
  .feature-list li svg { position: absolute; left: 0; top: 4px; }
  .feature-list strong { font-weight: 600; }
  .family-photo {
    position: absolute; left: 32px; top: 759px; width: 347px; height: 381px;
    border-radius: 6px;
    background: linear-gradient(165deg, #4a4d55 0%, #383a40 35%, #8a6a4a 55%, #2d2f34 78%, #3f8e96 100%);
    opacity: .93;
  }
  .footer-visit {
    position: absolute; left: 36px; top: 1150px; width: 390px;
    color: var(--white); font-size: 15px; line-height: 21px;
  }
  .footer-offer {
    position: absolute; left: 440px; top: 1110px; width: 370px;
    color: var(--white); font-size: 15px; line-height: 22px; text-align: justify;
  }
</style>
</head>
<body>
<main class="flyer">
  <div class="hero-scene" role="img" aria-label="Backyard swimming pool with ladder and calm water at sunset"></div>
  <div class="bar-photo" role="img" aria-label="Solar powered garden bar with dark shingled roof and panels, wood shelves, TV showing a football game, guests on bar stools and a dog lying beside it"></div>

  <header class="headline">
    <p class="headline-script">Your pool is lonely!</p>
    <h1 class="headline-intro">
      <span class="dark">Introducing our</span><br>
      <span class="accent">Stunning solar powered</span><br>
      <span class="accent">Garden Nook Tavern!</span>
    </h1>
  </header>

  <svg class="top-wave" width="846" height="100" viewBox="0 0 846 100" aria-hidden="true">
    <path d="M0 48 C200 14 420 96 846 52 L846 100 L0 100 Z" fill="#ffffff"/>
    <path d="M0 38 C200 4 420 86 846 42" fill="none" stroke="#1ba3ab" stroke-width="14"/>
    <path d="M0 56 C220 22 440 102 846 60" fill="none" stroke="#8fd3d6" stroke-width="4"/>
  </svg>

  <div class="brand-badge">Bright Cabin Works</div>

  <h2 class="section-heading">
    <span class="accent">Expand the value of</span><br>
    <span class="dark">your outdoor living with</span><br>
    <span class="accent">the ultimate Entertianment venue</span>
  </h2>

  <p class="intro-copy">Solar versions have enough solar and batteries to power your TV, lights, mini fridge, cell phones and more. The advanced Lithium Phosphate Batteries are very safe and can power everything for up to 48 hours without sun.</p>

  <div class="detail-photo detail-cooler" role="img" aria-label="Red cooler on the bar counter"></div>
  <div class="detail-photo detail-opener" role="img" aria-label="Hand using a wall bottle opener next to a football"></div>
  <div class="detail-photo detail-wine" role="img" aria-label="Wood wine shelf with bottles and hanging copper glasses"></div>

  <svg class="bottom-wave" width="846" height="270" viewBox="0 0 846 270" aria-hidden="true">
    <defs>
      <linearGradient id="footerTeal" x1="0" y1="0" x2="0" y2="1">
        <stop offset="0" stop-color="#1ba3ab"/>
        <stop offset="1" stop-color="#0a5f6c"/>
      </linearGradient>
    </defs>
    <path d="M0 100 C280 40 540 190 846 92 L846 270 L0 270 Z" fill="url(#footerTeal)"/>
    <path d="M0 86 C280 26 540 176 846 78" fill="none" stroke="#8fd3d6" stroke-width="5"/>
  </svg>

  <ul class="feature-list">
    <li><svg width="13" height="13" viewBox="0 0 13 13"><circle cx="6.5" cy="6.5" r="6.5" fill="#1ba3ab"/><path d="M3.5 6.8l2 2 4-4.2" fill="none" stroke="#fff" stroke-width="1.6"/></svg><strong>DIMENSIONS:</strong> 5′ deep x 10′ wide x 9-6′. Enough seating for 6-8 people.</li>
    <li><svg width="13" height="13" viewBox="0 0 13 13"><circle cx="6.5" cy="6.5" r="6.5" fill="#1ba3ab"/><path d="M3.5 6.8l2 2 4-4.2" fill="none" stroke="#fff" stroke-width="1.6"/></svg>Comes FULLY assembled. You can't reach this level of quality in a kit.</li>
    <li><svg width="13" height="13" viewBox="0 0 13 13"><circle cx="6.5" cy="6.5" r="6.5" fill="#1ba3ab"/><path d="M3.5 6.8l2 2 4-4.2" fill="none" stroke="#fff" stroke-width="1.6"/></svg>1 coat of primer, two coats of Havelock Prime Glossmark paint for extreme weather.</li>
    <li><svg width="13" height="13" viewBox="0 0 13 13"><circle cx="6.5" cy="6.5" r="6.5" fill="#1ba3ab"/><path d="M3.5 6.8l2 2 4-4.2" fill="none" stroke="#fff" stroke-width="1.6"/></svg>150 MPH rated Brantley Hale shingles</li>
    <li><svg width="13" height="13" viewBox="0 0 13 13"><circle cx="6.5" cy="6.5" r="6.5" fill="#1ba3ab"/><path d="M3.5 6.8l2 2 4-4.2" fill="none" stroke="#fff" stroke-width="1.6"/></svg>TV mount included in the base configuration.</li>
    <li><svg width="13" height="13" viewBox="0 0 13 13"><circle cx="6.5" cy="6.5" r="6.5" fill="#1ba3ab"/><path d="M3.5 6.8l2 2 4-4.2" fill="none" stroke="#fff" stroke-width="1.6"/></svg>Options include, pendant lights, hard surface floor, flip up shelf on short side, bar stools, cabinets, portable sinks, keg tap installs. wine shelves , copper wine glasses, liquor shelves and more!</li>
  </ul>

  <div class="family-photo" role="img" aria-label="Garden bar with family and children gathered at the counter, potted mums and small pumpkins in front"></div>

  <p class="footer-visit">Visit www.BrightCabinWorks.example/GardenNookTavern<br>to learn more!</p>
  <p class="footer-offer">Visit our website and mention "Coastal Glow" in the comments section and receive a free Kodo cooler when you order your new Garden Nook Tavern!</p>
</main>
</body>
</html>
```